Business Cards for Communications Technology Company

We are an innovative software company based in Tropical North Queensland, Australia. We have several brands with a focus on communications software for businesses. We are looking for a business card that is very innovate and creative whilst still remaining professional on a corporate level.

Our internal culture is very progressive and expresses a blend between the clarity of our natural surroundings and the highly technological industry we work in. Our current branding blends a modern minimalist typeface with the desire to push the boundaries in the way we communicate.

This is a corporate level business card for the communications software industry and may possibly also encompass our brands PelNetwork, PelCopy, PelPost and our B2B marketing service—with our companies name being Tarvix Holdings. Showing other brands on the business card is optional not compulsory.

Technical notes:

-We will attach all logo's and some examples of our corporate branding
- Would be willing to print with various papers, embossed, metallic ink, curved edges etc. in a standard business card size

Sample content:

Dorian Malcott
Senior Account Manager
Phone: 1300 482 916 / +617 4385 2604
Email: d.malcott@tarvix.com.au
Web: www.tarvix.com.au

Sincerely,
Tarvix Holdings.

```html
<!DOCTYPE html>
<html lang="en">
<head>
<meta charset="utf-8">
<title>Tarvix Holdings – Business Cards</title>
<link href="https://fonts.googleapis.com/css2?family=Roboto:wght@300;400;500;700&display=swap" rel="stylesheet">
<style>
  :root {
    --leaf: #7dc242;
    --leaf-dark: #6cb232;
    --paper: #ffffff;
    --backdrop: #eceae4;
    --ink: #3a3a3a;
    --ink-soft: #5a5a5a;
    --icon-blue: #3a6fc4;
  }
  * { box-sizing: border-box; margin: 0; padding: 0; }
  html, body { width: 1200px; height: 929px; overflow: hidden; }
  body {
    background: var(--backdrop);
    font-family: "Roboto", Arial, sans-serif;
    display: flex;
    align-items: center;
    justify-content: center;
    gap: 40px;
  }
  .card {
    position: relative;
    width: 540px;
    height: 300px;
    box-shadow: 0 6px 18px rgba(0,0,0,.18);
  }
  .card-frame {
    position: absolute;
    inset: 16px;
    border: 1px solid;
  }

  /* Front */
  .card-front { background: var(--leaf); color: var(--paper); }
  .card-front .card-frame { border-color: rgba(255,255,255,.85); }
  .wordmark {
    position: absolute;
    left: 0; right: 0;
    display: flex;
    align-items: center;
    justify-content: center;
    gap: 12px;
    font-weight: 500;
    letter-spacing: .5px;
  }
  .card-front .wordmark { top: 104px; font-size: 38px; }
  .wordmark-dot {
    width: 34px; height: 34px;
    border-radius: 50%;
    background: currentColor;
    flex: none;
  }
  .brand-row {
    position: absolute;
    left: 40px; right: 40px; bottom: 42px;
    display: flex;
    justify-content: space-between;
    font-weight: 700;
    font-size: 17px;
  }

  /* Back */
  .card-back { background: var(--paper); color: var(--ink); }
  .card-back .card-frame { border-color: var(--leaf); }
  .card-back .wordmark {
    left: 36px; right: auto;
    top: 170px;
    font-size: 26px;
    color: var(--ink);
  }
  .card-back .wordmark-dot { width: 24px; height: 24px; }
  .divider {
    position: absolute;
    left: 262px; top: 70px;
    width: 1px; height: 164px;
    background: var(--ink);
  }
  .contact {
    position: absolute;
    left: 282px; top: 66px;
    font-size: 12.5px;
    line-height: 1.4;
  }
  .contact-name {
    color: var(--leaf);
    font-weight: 500;
    font-size: 16px;
    letter-spacing: .3px;
  }
  .contact-title { font-weight: 700; font-size: 13px; margin-bottom: 12px; }
  .contact-address { color: var(--ink-soft); font-weight: 300; margin-bottom: 6px; }
  .contact-list { list-style: none; color: var(--ink-soft); font-weight: 300; }
  .contact-list li { display: flex; align-items: center; gap: 8px; }
  .contact-list svg { width: 11px; height: 11px; flex: none; }
</style>
</head>
<body>

  <section class="card card-front" aria-label="Business card front">
    <div class="card-frame"></div>
    <div class="wordmark"><span class="wordmark-dot"></span>Tarvix Holdings</div>
    <div class="brand-row">
      <span>PelPost</span>
      <span>PelCopy</span>
      <span>PelNetwork</span>
    </div>
  </section>

  <section class="card card-back" aria-label="Business card back">
    <div class="card-frame"></div>
    <div class="wordmark"><span class="wordmark-dot"></span>Tarvix Holdings</div>
    <div class="divider"></div>
    <div class="contact">
      <p class="contact-name">DORIAN MALCOTT</p>
      <p class="contact-title">Senior Account Manager</p>
      <p class="contact-address">Suite B4 58 Reef Rd,<br>Cairns. QLD 4870</p>
      <ul class="contact-list">
        <li>
          <svg viewBox="0 0 12 12" aria-hidden="true"><path d="M2.5 1 L4.5 1 L5 3.5 L3.8 4.5 Q5 7 7.5 8.2 L8.5 7 L11 7.5 L11 9.5 Q11 11 9.5 11 Q1 10 1 2.5 Q1 1 2.5 1Z" fill="var(--icon-blue)"/></svg>
          1300 482 916
        </li>
        <li>
          <svg viewBox="0 0 12 12" aria-hidden="true"><rect x="3" y="0.8" width="6" height="10.4" rx="1" fill="none" stroke="var(--icon-blue)" stroke-width="1.2"/><circle cx="6" cy="9.3" r=".7" fill="var(--icon-blue)"/></svg>
          +617 4385 2604
        </li>
        <li>
          <svg viewBox="0 0 12 12" aria-hidden="true"><rect x="0.8" y="2.5" width="10.4" height="7" fill="var(--icon-blue)"/><path d="M0.8 2.5 L6 6.5 L11.2 2.5" fill="none" stroke="#fff" stroke-width="1"/></svg>
          d.malcott@tarvix.com.au
        </li>
        <li>
          <svg viewBox="0 0 12 12" aria-hidden="true"><circle cx="6" cy="6" r="5" fill="none" stroke="var(--icon-blue)" stroke-width="1.1"/><ellipse cx="6" cy="6" rx="2.2" ry="5" fill="none" stroke="var(--icon-blue)" stroke-width=".9"/><path d="M1 6 H11" stroke="var(--icon-blue)" stroke-width=".9"/></svg>
          www.tarvix.com.au
        </li>
      </ul>
    </div>
  </section>

</body>
</html>
```